BrightPath Medical Exercise, LLC specializes in post rehab medical exercise for clients who have been discharged from physical therapy and/or other medical services and are in need of continued cardiovascular, strength, flexibility, endurance training and management of their medical conditions. We strive to bridge the gap between healthcare and fitness by staying in communication with the referring physician and /or physical therapist with updated progress notes to follow each clients progression, making sure each client is appropriate for exercise and identifying any red flags throughout the initial assessment and screening of the client, and referring those clients back to the physician and/or therapist when necessary.
Colors
Designer to choose colors to be used in the design.
Requirements
Must have
- Pictures of a trainer working with a client one on one during exercise, and group exercise
Nice to have
- Pictures that portray the bridge between healthcare and fitness
Should not have
- Cursive writing

```html
<!DOCTYPE html>
<html lang="en">
<head>
<meta charset="utf-8">
<title>BrightPath Medical Exercise – Rack Card</title>
<link href="https://fonts.googleapis.com/css2?family=Lato:ital,wght@0,300;0,400;0,700;0,900;1,300;1,700;1,900&family=Merriweather:ital,wght@1,900&display=swap" rel="stylesheet">
<style>
  :root{
    --red:#e0514a;
    --navy:#1f2a3d;
    --paper:#f1efea;
    --ink:#3a3f4a;
    --stage:#dcdde1;
    --white:#ffffff;
  }
  *{box-sizing:border-box;margin:0;padding:0}
  html,body{width:1200px;height:1200px;overflow:hidden;background:var(--stage)}
  .rack-card{
    position:absolute;left:300px;top:20px;width:600px;height:1160px;
    background:var(--paper);overflow:hidden;
    font-family:'Lato',sans-serif;color:var(--ink);
    box-shadow:0 6px 20px rgba(0,0,0,.18);
  }
  .hero-photo{
    position:absolute;left:0;top:0;width:600px;height:280px;
    background:linear-gradient(160deg,#3b3350 0%,#6e5a6a 35%,#a77d7a 55%,#4a5f6b 80%,#2c2f3d 100%);
  }
  .hero-waves{position:absolute;left:0;top:150px;width:600px;height:160px}
  .brand{position:absolute;left:0;top:162px;width:600px;text-align:center}
  .brand-mark{
    width:104px;height:104px;border-radius:50%;margin:0 auto;
    background:var(--white);border:6px solid var(--red);
  }
  .brand-name{
    margin-top:4px;font-weight:900;font-size:10.5px;line-height:1.1;
    color:var(--navy);text-transform:uppercase;letter-spacing:.3px;
  }
  .tagline{
    position:absolute;left:20px;top:318px;width:560px;text-align:center;
    font-family:'Merriweather',serif;font-style:italic;font-weight:900;
    font-size:20px;line-height:1.3;color:var(--navy);text-transform:uppercase;
  }
  .section-title{
    position:absolute;left:36px;width:540px;
    font-weight:900;font-size:20px;line-height:26px;color:var(--red);text-transform:uppercase;
  }
  .services-title{top:378px;left:44px}
  .conditions-title{top:487px}
  .services{position:absolute;left:38px;top:410px;list-style:none}
  .services li{
    font-style:italic;font-weight:300;font-size:15.5px;line-height:20.5px;color:var(--ink);
    display:flex;align-items:center;gap:5px;
  }
  .services svg{width:14px;height:12px;flex:none}
  .conditions{
    position:absolute;left:34px;top:565px;width:550px;
    display:grid;grid-template-columns:1fr 1fr;column-gap:20px;
  }
  .conditions ul{list-style:none}
  .conditions li{
    font-style:italic;font-weight:300;font-size:16px;line-height:22.4px;color:var(--ink);
    display:flex;align-items:center;
  }
  .conditions li::before{
    content:"";width:9px;height:9px;border-radius:50%;background:var(--red);
    margin-right:14px;flex:none;
  }
  .footer-waves{position:absolute;left:0;top:890px;width:600px;height:270px}
  .quote{position:absolute;left:70px;top:920px;width:460px;text-align:center}
  .quote p{font-style:italic;font-weight:900;font-size:18px;line-height:1.4;color:var(--navy)}
  .quote cite{
    display:block;font-style:normal;font-weight:400;font-size:18px;color:var(--ink);margin-top:0;
  }
  .quote-mark{
    position:absolute;font-family:'Merriweather',serif;font-weight:900;font-style:italic;
    font-size:64px;line-height:1;color:var(--navy);
  }
  .quote-open{left:-8px;top:-14px}
  .quote-close{right:-26px;top:14px}
  .contact{position:absolute;left:0;top:1058px;width:600px;height:60px;color:var(--white)}
  .contact-phone{
    position:absolute;left:56px;top:12px;display:flex;align-items:center;gap:10px;
    font-weight:700;font-style:italic;font-size:24px;
  }
  .contact-online{position:absolute;left:340px;top:4px;font-size:17px;line-height:24px;font-weight:400}
  .contact-online div{display:flex;align-items:center;gap:8px}
  .contact svg{flex:none}
</style>
</head>
<body>
<main class="rack-card">
  <div class="hero-photo" role="img" aria-label="Photo of a group exercise class using resistance bands, a woman in the foreground pulling a band overhead"></div>

  <svg class="hero-waves" viewBox="0 0 600 190" preserveAspectRatio="none" aria-hidden="true">
    <path d="M0 120 C120 90 200 60 300 95 C400 125 500 40 600 20 L600 190 L0 190 Z" fill="var(--white)"/>
    <path d="M0 160 C120 130 220 110 300 120 C420 135 520 150 600 60 L600 120 C530 190 430 160 320 140 C220 125 120 150 0 180 Z" fill="var(--red)"/>
    <path d="M0 170 C130 140 230 125 310 132 C430 145 530 170 600 95 L600 190 L0 190 Z" fill="var(--paper)"/>
    <path d="M530 150 C560 140 585 120 600 95 L600 110 C585 135 560 150 530 158 Z" fill="var(--navy)"/>
  </svg>

  <div class="brand">
    <div class="brand-mark"></div>
    <div class="brand-name">BrightPath<br>Medical Exercise</div>
  </div>

  <h1 class="tagline">„Getting you back to function as<br>quickly and safely as possible”</h1>

  <h2 class="section-title services-title">Our products and services:</h2>
  <ul class="services">
    <li><svg viewBox="0 0 14 12"><path d="M1 6 L5 10 L13 1" fill="none" stroke="var(--red)" stroke-width="2.4"/></svg>Initial Assessment and Functional Screening</li>
    <li><svg viewBox="0 0 14 12"><path d="M1 6 L5 10 L13 1" fill="none" stroke="var(--red)" stroke-width="2.4"/></svg>One-On-One supervised post rehab exercise</li>
    <li><svg viewBox="0 0 14 12"><path d="M1 6 L5 10 L13 1" fill="none" stroke="var(--red)" stroke-width="2.4"/></svg>Online consultation with individualized home exercise program</li>
  </ul>

  <h2 class="section-title conditions-title">We offer management of the<br>following conditions and more:</h2>
  <div class="conditions">
    <ul>
      <li>Diabetes</li>
      <li>Hypertension</li>
      <li>ACL Rupture</li>
      <li>Ankle Fracture</li>
      <li>Bicipital Tendonitis</li>
      <li>Total Hip Replacement</li>
      <li>Total Knee Replacement</li>
      <li>Spinal Stenosis</li>
      <li>Multiple Sclerosis</li>
      <li>Shoulder Dislocation</li>
      <li>Scoliosis</li>
      <li>Osteoporosis</li>
      <li>Osteoarthritis</li>
      <li>Cervical disc herniation</li>
    </ul>
    <ul>
      <li>AC Joint Separation</li>
      <li>Fibromyalgia</li>
      <li>Spondylothesis</li>
      <li>Parkinson’s Disease</li>
      <li>Tibial Plateau Fracture</li>
      <li>Tennis Elbow/Golfer’s Elbow</li>
      <li>Carpal Tunnel Syndrome</li>
      <li>Total Shoulder Replacement</li>
      <li>Bicipital Tendonitis</li>
      <li>Patello-Femoral Syndrome</li>
      <li>Rotator Cuff Syndrome</li>
      <li>Cervical Strain</li>
      <li>Impingement Syndrome</li>
      <li>Laminectomy</li>
    </ul>
  </div>

  <svg class="footer-waves" viewBox="0 0 600 270" preserveAspectRatio="none" aria-hidden="true">
    <path d="M0 110 C20 40 55 0 85 30 C140 95 220 140 320 140 C430 140 520 90 600 70 L600 270 L0 270 Z" fill="var(--red)"/>
    <path d="M0 150 C30 80 65 50 95 75 C150 125 230 150 330 148 C440 145 520 100 600 85 L600 97 C520 112 440 158 330 162 C230 165 150 140 95 92 C65 68 30 105 0 170 Z" fill="var(--paper)"/>
  </svg>

  <blockquote class="quote">
    <span class="quote-mark quote-open">“</span>
    <p>Exercise is the key to long-term<br>management of most medical conditions</p>
    <cite>~ Daniel R Hayes, PhD, PT</cite>
    <span class="quote-mark quote-close">”</span>
  </blockquote>

  <footer class="contact">
    <div class="contact-phone">
      <svg width="30" height="30" viewBox="0 0 30 30"><path d="M7 3 L11 3 L13 9 L10 11 C11 15 15 19 19 20 L21 17 L27 19 L27 23 C27 25 25 27 23 27 C12 26 4 18 3 7 C3 5 5 3 7 3 Z" fill="none" stroke="var(--white)" stroke-width="2"/><path d="M18 3 A9 9 0 0 1 27 12 M18 7 A5 5 0 0 1 23 12" fill="none" stroke="var(--white)" stroke-width="2"/></svg>
      (555) 014-2870
    </div>
    <div class="contact-online">
      <div><svg width="18" height="18" viewBox="0 0 18 18"><circle cx="9" cy="9" r="7.5" fill="none" stroke="var(--white)" stroke-width="1.3"/><ellipse cx="9" cy="9" rx="3.5" ry="7.5" fill="none" stroke="var(--white)" stroke-width="1.3"/><path d="M1.5 9 H16.5 M3 5 H15 M3 13 H15" stroke="var(--white)" stroke-width="1.1"/></svg>www.brightpathmedex.com</div>
      <div><svg width="18" height="14" viewBox="0 0 18 14"><rect x="1" y="1" width="16" height="12" fill="none" stroke="var(--white)" stroke-width="1.3"/><path d="M1 1 L9 8 L17 1" fill="none" stroke="var(--white)" stroke-width="1.3"/></svg>hello@brightpathmedex.com</div>
    </div>
  </footer>
</main>
</body>
</html>
```